Talbrin Business Cards

Front and back. Simon Kavelle MBA is the CEO of Talbrin Homes. Black white and grays. Logo and cool design.

Target Market(s)

Professional lenders and investors

Industry/Entity Type

Real estate developer. NO HOUSES OR ROOFS

Contact Information for Business Card

Logo, name and unique design. Front and back. Simon Kavelle MBA is the CEO of Talbrin Homes. Black white and grays. Logo and cool design.

Font styles to use
Sans Serif

Colors

Designer to choose only greyscale colors for use in the design.

Requirements
Must have
• Cool look. Not the same card I could design.
Nice to have
• Something memorable
Should not have
• Basic

```html
<!DOCTYPE html>
<html lang="en">
<head>
<meta charset="utf-8">
<title>Talbrin Business Cards</title>
<link href="https://fonts.googleapis.com/css2?family=Montserrat:wght@400;600;800&display=swap" rel="stylesheet">
<style>
  :root {
    --ink: #080808;
    --paper: #ffffff;
    --stripe: #5a5a5a;
    --backdrop: #3b3b3b;
    --muted: #d4d4d4;
  }
  html, body {
    margin: 0;
    width: 1200px;
    height: 1200px;
    overflow: hidden;
    background: var(--backdrop);
    font-family: "Montserrat", sans-serif;
  }
  .card {
    position: absolute;
    left: 250px;
    width: 700px;
    height: 400px;
    border-radius: 26px;
    overflow: hidden;
  }
  .card--front { top: 140px; background: var(--paper); }
  .card--back { top: 620px; background: var(--ink); }
  .card__shapes { position: absolute; inset: 0; }
  .wordmark {
    position: absolute;
    font-weight: 800;
    letter-spacing: -0.5px;
    white-space: nowrap;
    line-height: 1;
  }
  .card--front .wordmark {
    left: 452px;
    right: 24px;
    top: 128px;
    text-align: center;
    font-size: 30px;
    color: var(--ink);
  }
  .card--back .wordmark {
    left: 0;
    right: 0;
    top: 162px;
    text-align: center;
    font-size: 72px;
    color: var(--paper);
  }
  .contact {
    position: absolute;
    left: 48px;
    top: 210px;
    color: var(--paper);
  }
  .contact__name {
    margin: 0;
    font-size: 21px;
    font-weight: 800;
    letter-spacing: 0.5px;
  }
  .contact__role {
    margin: 2px 0 22px;
    font-size: 13px;
    font-weight: 400;
    color: var(--muted);
    letter-spacing: 0.5px;
  }
  .contact__list { list-style: none; margin: 0; padding: 0; }
  .contact__item {
    display: flex;
    align-items: center;
    gap: 10px;
    font-size: 17px;
    margin-bottom: 6px;
  }
  .contact__icon { width: 18px; height: 18px; flex: none; }
</style>
</head>
<body>

<section class="card card--front">
  <svg class="card__shapes" viewBox="0 0 700 400" aria-hidden="true">
    <polygon points="0,0 292,0 410,168 446,400 0,400" fill="var(--ink)"/>
    <polygon points="304,0 318,0 436,168 474,400 460,400 424,168" fill="var(--stripe)"/>
  </svg>
  <div class="wordmark">Talbrin Homes</div>
  <div class="contact">
    <h1 class="contact__name">SIMON KAVELLE, MBA</h1>
    <p class="contact__role">CEO | TALBRIN HOMES</p>
    <ul class="contact__list">
      <li class="contact__item">
        <svg class="contact__icon" viewBox="0 0 24 24"><path fill="var(--paper)" d="M6.6 10.8a15 15 0 0 0 6.6 6.6l2.2-2.2a1 1 0 0 1 1-.25 11.4 11.4 0 0 0 3.6.57 1 1 0 0 1 1 1V20a1 1 0 0 1-1 1A17 17 0 0 1 3 4a1 1 0 0 1 1-1h3.5a1 1 0 0 1 1 1c0 1.25.2 2.45.57 3.57a1 1 0 0 1-.25 1z"/></svg>
        +1 555-310-4200
      </li>
      <li class="contact__item">
        <svg class="contact__icon" viewBox="0 0 24 24"><rect x="2" y="5" width="20" height="14" rx="1" fill="none" stroke="var(--paper)" stroke-width="2"/><path d="M2 6l10 7 10-7" fill="none" stroke="var(--paper)" stroke-width="2"/></svg>
        Simon@TalbrinHomes.com
      </li>
      <li class="contact__item">
        <svg class="contact__icon" viewBox="0 0 24 24" fill="none" stroke="var(--paper)" stroke-width="1.6"><circle cx="12" cy="12" r="10"/><ellipse cx="12" cy="12" rx="4.5" ry="10"/><path d="M2 12h20M4 7h16M4 17h16"/></svg>
        www.talbrinhomes.com
      </li>
    </ul>
  </div>
</section>

<section class="card card--back">
  <div class="wordmark">Talbrin Homes</div>
</section>

</body>
</html>
```